Jägerbrief
Zielgruppe
Es soll ein 'Jägerbrief' werden. Diesen Jägerbrief erhält ein Jäger, wenn er sein erstes Stück Wild auf einer Jagd erlegen konnte.
Aufgabenstellung
Das Design ist im Format einer Urkunde auszuhändigen und sollte gerne in einem traditionellen Design gemacht werden. Beispielbilder sind im Anhang und können gerne als Inspiration genommen werden.
Genaue Details:
Überschrift in groß 'Jägerbrief'
Darunter den Text zentriert wie folgt abbilden:
'Im Revier von Tannwöhrden, gelegen im Herzen von Grevenmarsch, tratst du,
zur Niederwildjagd an und bewiesest dein Können, deinen Respekt vor der Natur und deine Geduld im Angesicht der Herausforderung.
An diesem besonderen Tag hattest du die Ehre, deinen ersten Feldhasen zu strecken. Mit diesem Erfolg trittst du in die stolze Tradition der Waidmänner ein, die die Schönheit und den Wert unserer heimischen Wildbestände zu schätzen wissen und Verantwortung für deren Erhalt übernehmen.
Möge dieser Moment dir stets in Erinnerung bleiben und dir ein Ansporn sein, die Jagd mit Demut, Leidenschaft und Verantwortung auszuüben.
Mit diesem Jägerbrief gratulieren wir dir herzlich zu deinem ersten Feldhasen und wünschen dir weiterhin Waidmannsheil auf all deinen Wegen im Revier.
Hochachtungsvoll und mit Waidmannsgruß
Die Jagdgesellschaft von Tannwöhrden'

```html
<!DOCTYPE html>
<html lang="de">
<head>
<meta charset="utf-8">
<title>Jägerbrief</title>
<link rel="stylesheet" href="https://fonts.googleapis.com/css2?family=UnifrakturMaguntia&family=Parisienne&display=swap">
<style>
  :root {
    --sepia-light: #e8d6bf;
    --sepia-mid: #c9a98a;
    --sepia-dark: #8a5a45;
    --panel: rgba(255, 250, 244, 0.55);
    --title-ink: #102a25;
    --body-ink: #2b1d15;
  }
  html, body {
    margin: 0;
    padding: 0;
    width: 849px;
    height: 1200px;
    overflow: hidden;
    background: var(--sepia-light);
  }
  .certificate {
    position: relative;
    width: 849px;
    height: 1200px;
    overflow: hidden;
  }
  .forest-scene {
    position: absolute;
    inset: 0;
    background:
      radial-gradient(ellipse at 50% 45%, rgba(240, 224, 204, 0.9) 0%, rgba(240, 224, 204, 0) 55%),
      linear-gradient(180deg, #dcc3a6 0%, #e6d2ba 30%, #cfae90 65%, #a77a60 100%);
  }
  .forest-scene .edge {
    position: absolute;
    top: 0;
    bottom: 0;
    width: 180px;
  }
  .forest-scene .edge.left { left: 0; background: linear-gradient(90deg, rgba(138, 90, 69, 0.55), rgba(138, 90, 69, 0)); }
  .forest-scene .edge.right { right: 0; background: linear-gradient(270deg, rgba(138, 90, 69, 0.55), rgba(138, 90, 69, 0)); }
  .text-panel {
    position: absolute;
    left: 163px;
    top: 225px;
    width: 518px;
    height: 748px;
    background: var(--panel);
  }
  .title {
    position: absolute;
    left: 0;
    right: 0;
    top: 108px;
    margin: 0;
    text-align: center;
    font-family: "UnifrakturMaguntia", serif;
    font-weight: 400;
    font-size: 74px;
    line-height: 1;
    color: var(--title-ink);
  }
  .title .initial {
    font-size: 150px;
    vertical-align: -42px;
  }
  .letter {
    position: absolute;
    left: 163px;
    width: 518px;
    top: 305px;
    text-align: center;
    font-family: "Parisienne", cursive;
    font-size: 15px;
    line-height: 24.5px;
    color: var(--body-ink);
  }
  .letter p { margin: 0 0 24.5px; }
  .letter .date-gap { height: 50px; }
  .letter .closing { margin-bottom: 24px; }
</style>
</head>
<body>
<main class="certificate">
  <div class="forest-scene" role="img" aria-label="Gestochene Waldszene in Sepia mit Hirschen, Rehen, einem Feldhasen und Jagdhund zwischen hohen Bäumen">
    <div class="edge left"></div>
    <div class="edge right"></div>
  </div>

  <div class="text-panel"></div>

  <h1 class="title"><span class="initial">J</span>ägerbrief</h1>

  <section class="letter">
    <p>Im Revier von Tannwöhrden, gelegen im Herzen von Grevenmarsch,<br>tratst du, am</p>
    <div class="date-gap"></div>
    <p>zur Niederwildjagd an und bewiesest dein Können, deinen Respekt<br>vor der Natur und deine Geduld im Angesicht der<br>Herausforderung.</p>
    <p>An diesem besonderen Tag hattest du die Ehre, deinen ersten<br>Feldhasen zu strecken. Mit diesem Erfolg trittst du in die stolze<br>Tradition der Waidmänner ein, die die Schönheit und den Wert<br>unserer heimischen Wildbestände zu schätzen wissen und<br>Verantwortung für deren Erhalt übernehmen.</p>
    <p>Möge dieser Moment dir stets in Erinnerung bleiben und dir ein<br>Ansporn sein, die Jagd mit Demut, Leidenschaft und<br>Verantwortung auszuüben.</p>
    <p>Mit diesem Jägerbrief gratulieren wir dir herzlich zu deinem ersten<br>Feldhasen und wünschen dir weiterhin Waidmannsheil auf all deinen<br>Wegen im Revier.</p>
    <p class="closing">Hochachtungsvoll und mit Waidmannsgruß</p>
    <p class="signature">Die Jagdgesellschaft von Tannwöhrden</p>
  </section>
</main>
</body>
</html>
```